Hello Creative Minds!
Our business is after a elegant and classy flyer that draws attention!
The business is Velmora Turf - Lawn Rejuvenation Services. We provide services that maintain a healthy and vibrant green lawn through the tough Australian seasons. The products we use limits the water needed to keep grass green to a minimum - practically none at all! This not only helps the home owner or home seller but the environment by limiting the use of water that is needed to create a green lawn. The products we use are made from natural ingredients that are and pet friendly.
This fly will be our introductory offer to the market. Below are the required points that need to be on the flyer. Attached is the business logo, before & after pictures and 1 example of the LAYOUT not DESIGN of what the flyer should be laid out like or similar to. Feel free to use different 'Lawn Mower' pictures.
All the best; if you need any questions answered please feel free to message.
REQUIRED POINTS (Please re-phrase were possible);
*Instantly restores the natural green colour of grass – year round
*Lasts for up to 3 months
*Substantially reduces watering needs
*Pet friendly
*Stays green during droughts and water restrictions
*UV fade resistant
*Won’t bleed, run, or stain once absorbed into the grass
*Safe for the environment, pets and people
*Works in extreme heat, cold and frost
*Organic and natural – no harmful chemicals
*Reduces the amount of fertilizer
and water used on lawns
*Kerb appeal is essential for getting your property sold for the highest price possible
SERVICES & PRICING
Lawn maintenance (cut & trim) starting from $60
Lawn rejuvenation starting from $80 (Only $27 a month for 3 months)*
Package deal starting from $120
Introductory offer: 25% off all services. Refer a friend, when they book you receive another 25% off your next service.
LOCATIONS
Nowra to Sydney
CONTACT NUMBER
Will be posted with the winner - please leave an area for this.
SOCIAL MEDIA
Please add Chatterloop and Snapvista logo's
Updates
Competition has finished, thank you to all that have participated! I will review and comment on the flyers that need assistance. All the best with future designs!
Target Market(s)
home owners, home sellers, property developers, real estates and nursing homes and government housing.
Industry/Entity Type
Lawn Care
Look and feel
Each slider illustrates characteristics of the customer's brand and the style your logo design should communicate.

```html
<!DOCTYPE html>
<html lang="en">
<head>
<meta charset="utf-8">
<title>Velmora Turf - Lawn Rejuvenation Services</title>
<link rel="stylesheet" href="https://fonts.googleapis.com/css2?family=Roboto+Condensed:wght@400;700&family=Oswald:wght@500;700&family=Lato:wght@400;700&family=Roboto:wght@700&display=swap">
<style>
  :root{
    --backdrop:#2d2d2d;
    --green-dark:#1b8a13;
    --green-deep:#0f7a0c;
    --green-light:#8cc63f;
    --navy:#272d38;
    --ink:#1e1e1e;
    --white:#ffffff;
  }
  html,body{margin:0;padding:0;width:1200px;height:1200px;overflow:hidden;background:var(--backdrop);}
  .stage{position:relative;width:1500px;height:1500px;transform:scale(0.8);transform-origin:0 0;}
  .flyer{position:absolute;width:670px;height:860px;background:var(--white);overflow:hidden;}
  .flyer--features{left:58px;top:310px;}
  .flyer--pricing{left:770px;top:313px;width:668px;}
  .flyer svg.art{position:absolute;left:0;top:0;}

  .brand-name{position:absolute;left:40px;top:356px;width:260px;text-align:center;
    font-family:"Roboto Condensed",sans-serif;font-weight:400;font-size:40px;color:var(--white);}

  .headline{position:absolute;left:0;width:670px;top:515px;margin:0;text-align:center;
    font-family:"Roboto Condensed",sans-serif;font-weight:400;font-size:60px;color:var(--green-dark);letter-spacing:-0.5px;}

  .benefit{position:absolute;font-family:Lato,sans-serif;font-size:11px;line-height:13px;color:var(--ink);padding-left:13px;}
  .benefit::before{content:"";position:absolute;left:0;top:2px;width:7px;height:4px;border-left:2px solid var(--green-dark);border-bottom:2px solid var(--green-dark);transform:rotate(-45deg);}

  .call{position:absolute;right:55px;text-align:right;color:var(--white);font-family:Lato,sans-serif;}
  .call__label{font-size:24px;line-height:28px;}
  .call__phone{font-size:31px;font-weight:700;letter-spacing:3px;line-height:40px;}

  .photo-label{position:absolute;top:180px;font-family:Oswald,sans-serif;font-weight:700;font-size:52px;color:var(--white);}

  .section-title{position:absolute;left:0;width:630px;top:438px;margin:0;text-align:center;
    font-family:Oswald,sans-serif;font-weight:700;font-size:36px;letter-spacing:3px;color:var(--green-dark);}
  .section-rule{position:absolute;left:136px;top:484px;width:361px;height:4px;background:var(--navy);}

  .price-card{position:absolute;top:510px;width:178px;height:165px;border-radius:18px;overflow:hidden;
    font-family:"Roboto Condensed",sans-serif;color:var(--white);text-align:center;}
  .price-card__name{height:88px;background:var(--green-light);display:flex;align-items:center;justify-content:center;
    font-weight:700;font-size:23px;line-height:26px;}
  .price-card__price{height:77px;background:var(--green-dark);display:flex;flex-direction:column;align-items:center;justify-content:center;font-size:22px;}
  .price-card__note{font-size:12px;}

  .offer{position:absolute;left:28px;top:688px;width:620px;margin:0;font-family:Roboto,sans-serif;font-weight:700;
    font-size:12.5px;line-height:16px;letter-spacing:1.1px;color:var(--ink);}
</style>
</head>
<body>
<div class="stage">

  <section class="flyer flyer--features">
    <svg class="art" width="670" height="860" viewBox="0 0 670 860">
      <defs>
        <linearGradient id="lawnPhotoL" x1="0" y1="0" x2="0" y2="1">
          <stop offset="0" stop-color="#2b3a1e"/><stop offset="0.15" stop-color="#4f8f2a"/><stop offset="1" stop-color="#5fb53a"/>
        </linearGradient>
        <linearGradient id="ovalFill" x1="0" y1="0" x2="0" y2="1">
          <stop offset="0" stop-color="#3a414e"/><stop offset="1" stop-color="#1f242d"/>
        </linearGradient>
        <linearGradient id="grassL" x1="0" y1="0" x2="0" y2="1">
          <stop offset="0" stop-color="#b6e05a"/><stop offset="1" stop-color="#3f9b1c"/>
        </linearGradient>
      </defs>
      <path role="img" aria-label="Lawn mower cutting stripes on a bright green lawn" d="M0 0H670V300Q420 470 0 255Z" fill="url(#lawnPhotoL)"/>
      <path d="M0 262Q420 478 670 306" fill="none" stroke="var(--green-light)" stroke-width="10"/>
      <path d="M0 275Q420 492 670 318" fill="none" stroke="var(--green-dark)" stroke-width="8"/>
      <circle cx="580" cy="343" r="80" fill="var(--green-dark)"/>
      <circle role="img" aria-label="Person pushing an orange lawn mower" cx="580" cy="343" r="72" fill="#c98a45"/>
      <circle cx="477" cy="408" r="82" fill="var(--green-light)"/>
      <circle cx="477" cy="408" r="75" fill="var(--white)"/>
      <circle role="img" aria-label="Gardener tending a backyard lawn with a dog" cx="477" cy="408" r="68" fill="#6f9a4a"/>
      <ellipse cx="170" cy="390" rx="182" ry="112" fill="var(--green-dark)"/>
      <ellipse cx="170" cy="390" rx="172" ry="103" fill="var(--white)"/>
      <ellipse cx="170" cy="390" rx="165" ry="96" fill="url(#ovalFill)"/>
      <path role="img" aria-label="Field of grass blades" d="M0 730Q80 700 180 740Q260 720 330 760L330 860H0Z" fill="url(#grassL)"/>
      <path d="M300 860Q360 760 520 755Q620 752 670 735V860Z" fill="var(--green-deep)"/>
    </svg>
    <div class="brand-name">Velmora Turf</div>
    <h1 class="headline">Lawn Rejuvenation Services</h1>

    <div class="benefit" style="left:28px;top:594px;width:170px">Instantly restores the natural green colour of grass – year round</div>
    <div class="benefit" style="left:28px;top:631px;width:170px">Stays green during droughts and water restrictions</div>
    <div class="benefit" style="left:28px;top:671px;width:170px">Works in extreme heat, cold and frost</div>
    <div class="benefit" style="left:225px;top:596px;width:120px">Lasts for up to 3 months</div>
    <div class="benefit" style="left:225px;top:632px;width:120px">UV fade resistant</div>
    <div class="benefit" style="left:225px;top:672px;width:120px">Organic and natural – no harmful chemicals</div>
    <div class="benefit" style="left:355px;top:596px;width:155px">Substantially reduces watering needs</div>
    <div class="benefit" style="left:355px;top:632px;width:155px">Won't bleed, run, or stain once absorbed into the grass</div>
    <div class="benefit" style="left:355px;top:674px;width:155px">Reduces the amount of fertilizer and water used on lawns</div>
    <div class="benefit" style="left:520px;top:596px;width:130px">Pet friendly</div>
    <div class="benefit" style="left:520px;top:629px;width:130px">Safe for the environment, pets and people</div>
    <div class="benefit" style="left:520px;top:674px;width:130px">Kerb appeal is essential for getting your property sold for the highest price possible</div>

    <div class="call" style="top:772px">
      <div class="call__label">Call Now !</div>
      <div class="call__phone">123 456 7890</div>
    </div>
  </section>

  <section class="flyer flyer--pricing">
    <svg class="art" width="668" height="860" viewBox="0 0 668 860">
      <defs>
        <linearGradient id="dryGrass" x1="0" y1="0" x2="1" y2="1">
          <stop offset="0" stop-color="#bfa57a"/><stop offset="1" stop-color="#8f7752"/>
        </linearGradient>
        <linearGradient id="greenGrass" x1="0" y1="0" x2="1" y2="1">
          <stop offset="0" stop-color="#5a8f3c"/><stop offset="1" stop-color="#2f6b22"/>
        </linearGradient>
        <linearGradient id="grassR" x1="0" y1="0" x2="0" y2="1">
          <stop offset="0" stop-color="#b6e05a"/><stop offset="1" stop-color="#3f9b1c"/>
        </linearGradient>
      </defs>
      <path role="img" aria-label="Close-up of dry, brown grass before treatment" d="M0 0H330V395H0Z" fill="url(#dryGrass)"/>
      <path role="img" aria-label="Close-up of lush green grass after treatment" d="M336 0H668V395H336Z" fill="url(#greenGrass)"/>
      <path d="M0 330Q330 460 668 250V400H0Z" fill="var(--white)"/>
      <path d="M0 318Q330 445 668 245" fill="none" stroke="var(--green-light)" stroke-width="8"/>
      <path d="M0 332Q330 462 668 258" fill="none" stroke="var(--green-dark)" stroke-width="9"/>
      <circle cx="560" cy="375" r="88" fill="var(--green-dark)"/>
      <circle cx="560" cy="375" r="80" fill="var(--white)"/>
      <circle role="img" aria-label="Backyard with a freshly treated green lawn and grey fence" cx="560" cy="375" r="75" fill="#7d8580"/>
      <path role="img" aria-label="Field of grass blades" d="M0 730Q80 700 180 740Q260 720 330 760L330 860H0Z" fill="url(#grassR)"/>
      <path d="M300 860Q360 760 520 755Q620 752 668 735V860Z" fill="var(--green-deep)"/>
    </svg>
    <div class="photo-label" style="left:110px">Before</div>
    <div class="photo-label" style="left:436px">After</div>

    <h2 class="section-title">SERVICES &amp; PRICING</h2>
    <div class="section-rule"></div>

    <div class="price-card" style="left:32px">
      <div class="price-card__name">Lawn Maintenance<br>(cut &amp;amp ; trim)</div>
      <div class="price-card__price">starting from $60</div>
    </div>
    <div class="price-card" style="left:246px">
      <div class="price-card__name">Lawn<br>Rejuvenation</div>
      <div class="price-card__price">starting from $80<span class="price-card__note">(Only $27 a month for 3 months)*</span></div>
    </div>
    <div class="price-card" style="left:458px">
      <div class="price-card__name">Package<br>Deal</div>
      <div class="price-card__price">starting from $120</div>
    </div>

    <p class="offer">Introductory offer: 25% off all services. Refer a friend, when they book you receive another 25% off your next service</p>

    <div class="call" style="top:772px">
      <div class="call__label">Call Now !</div>
      <div class="call__phone">123 456 7890</div>
    </div>
  </section>

</div>
</body>
</html>
```